Vesit cards for web development company

We need a business card design for our company. The company develops online platforms and conducts marketing consulting. Company logo. The cards must fit in with us (a junior start UP), but they must also be professional enough to impress with investors like banks. We wish you a combination of classic and modern design

Target Market(s)

Business partners and IT and marketing customers

Industry/Entity Type

It Company

Contact Information for Business Card

Folgende Information müssen Drauf.
Name, Position, Telefon Nr., Mobile Nr., E-Mail adresse, Optional sind noch Webadresse und HRB Nummer

Colors

Designer to choose colors to be used in the design.

Requirements
Must have
• The cards have to fit into the logo later and have to be dynamic and serious at the same time

```html
<!DOCTYPE html>
<html lang="en">
<head>
<meta charset="UTF-8">
<title>Norvik Development – Business Card</title>
<link rel="stylesheet" href="https://fonts.googleapis.com/css2?family=Arimo:wght@400&family=Ubuntu:wght@500;700&display=swap">
<style>
  :root {
    --backdrop: #3a3a3c;
    --card: #1f1f21;
    --card-edge: #2a2a2c;
    --blue: #2a78b8;
    --text: #c9c9cb;
    --muted: #9a9a9c;
    --silver: #8d8e91;
  }
  * { box-sizing: border-box; margin: 0; padding: 0; }
  html, body { width: 799px; height: 1200px; overflow: hidden; }
  body {
    background: var(--backdrop);
    display: flex;
    flex-direction: column;
    align-items: center;
    justify-content: center;
    gap: 110px;
    font-family: "Arimo", Arial, sans-serif;
  }
  .card {
    position: relative;
    width: 600px;
    height: 343px;
    background: var(--card);
    border: 1px solid var(--card-edge);
    border-radius: 4px;
    box-shadow: 0 18px 40px rgba(0,0,0,0.45);
  }
  .card--front { display: flex; align-items: center; justify-content: center; }
  .front-mark {
    display: flex;
    align-items: center;
    gap: 12px;
    font-family: "Ubuntu", sans-serif;
    font-weight: 700;
    font-size: 56px;
    color: var(--silver);
    letter-spacing: 1px;
  }
  .front-mark .dot {
    width: 18px; height: 18px; border-radius: 50%;
    background: var(--silver);
  }
  .identity { position: absolute; left: 34px; top: 34px; }
  .identity .name {
    font-family: "Ubuntu", sans-serif;
    font-weight: 700;
    font-size: 21px;
    color: var(--blue);
  }
  .identity .role { font-size: 12px; color: var(--muted); margin-top: 3px; }
  .contact {
    position: absolute;
    left: 34px;
    top: 172px;
    font-size: 14px;
    line-height: 19px;
    color: var(--text);
    list-style: none;
  }
  .contact li { display: flex; align-items: center; gap: 8px; }
  .contact .label { color: var(--blue); }
  .contact svg { width: 13px; height: 13px; fill: var(--blue); flex: none; }
  .contact .plain { padding-left: 21px; }
  .brand {
    position: absolute;
    right: 36px;
    bottom: 36px;
    display: flex;
    align-items: center;
    gap: 10px;
    font-family: "Ubuntu", sans-serif;
    font-weight: 700;
    font-size: 30px;
    color: var(--blue);
    text-transform: uppercase;
  }
  .brand .square { width: 14px; height: 14px; background: var(--blue); }
</style>
</head>
<body>
  <section class="card card--front" aria-label="Card front">
    <div class="front-mark"><span class="dot"></span>Norvik</div>
  </section>

  <section class="card card--back" aria-label="Card back">
    <div class="identity">
      <p class="name">Lena Hartmann</p>
      <p class="role">Managing Director</p>
    </div>
    <ul class="contact">
      <li class="plain">Lindenweg 14</li>
      <li class="plain">40210 Düsseldorf</li>
      <li class="plain"><span class="label">HRB Nr.:</span>&nbsp;58213</li>
      <li>
        <svg viewBox="0 0 24 24"><path d="M6.6 10.8a15 15 0 0 0 6.6 6.6l2.2-2.2a1 1 0 0 1 1-.25 11.4 11.4 0 0 0 3.6.57 1 1 0 0 1 1 1V20a1 1 0 0 1-1 1A17 17 0 0 1 3 4a1 1 0 0 1 1-1h3.5a1 1 0 0 1 1 1c0 1.25.2 2.45.57 3.57a1 1 0 0 1-.25 1z"/></svg>
        0521 448 219
      </li>
      <li>
        <svg viewBox="0 0 24 24"><path d="M7 1h10a2 2 0 0 1 2 2v18a2 2 0 0 1-2 2H7a2 2 0 0 1-2-2V3a2 2 0 0 1 2-2zm0 3v14h10V4zm5 15.5a1 1 0 1 0 0 2 1 1 0 0 0 0-2z"/></svg>
        0176 302 954
      </li>
      <li>
        <svg viewBox="0 0 24 24"><path d="M2 5h20v14H2zm2 2v.5l8 5 8-5V7zm0 3v7h16v-7l-8 5z"/></svg>
        hello@norvikdev.com
      </li>
      <li>
        <svg viewBox="0 0 24 24"><path d="M12 2a10 10 0 1 0 0 20 10 10 0 0 0 0-20zm6.9 6h-3a15 15 0 0 0-1.3-3.9A8 8 0 0 1 18.9 8zM12 4c.8 1.2 1.5 2.5 1.9 4h-3.8c.4-1.5 1.1-2.8 1.9-4zM4.3 14a8 8 0 0 1 0-4h3.4a16 16 0 0 0 0 4zm.8 2h3a15 15 0 0 0 1.3 3.9A8 8 0 0 1 5.1 16zm3-8h-3a8 8 0 0 1 4.3-3.9A15 15 0 0 0 8.1 8zM12 20c-.8-1.2-1.5-2.5-1.9-4h3.8c-.4 1.5-1.1 2.8-1.9 4zm2.3-6H9.7a14 14 0 0 1 0-4h4.6a14 14 0 0 1 0 4zm.3 5.9a15 15 0 0 0 1.3-3.9h3a8 8 0 0 1-4.3 3.9zm1.7-5.9a16 16 0 0 0 0-4h3.4a8 8 0 0 1 0 4z"/></svg>
        www.norvikdev.com
      </li>
    </ul>
    <div class="brand"><span class="square"></span>Norvik Development</div>
  </section>
</body>
</html>
```